plumbing & gas fitting business card design

We need a business card design for a plumbing & gas fitting company. The company covers commercial, domestic and maintenance work. We would like a modern design communicating efficiency and sophistication. preferred colours would include (red grey & black) or (green grey & black). Please DO NOT include any water droplets.

Industry/Entity Type

Business

Contact Information for Business Card

Vortig Plumbing & Gas, Commercial Domestic & Maintenance, licence no. 617394K, ABN 47215830962, Phone 0417382956, Email vortigplumbingandgas@corvanet.com

```html
<!DOCTYPE html>
<html lang="en">
<head>
<meta charset="utf-8">
<title>Vortig Plumbing &amp; Gas — Stationery</title>
<link rel="stylesheet" href="https://fonts.googleapis.com/css2?family=Barlow:wght@600&family=Zilla+Slab:ital,wght@0,400;1,400&display=swap">
<style>
  :root {
    --backdrop: #efefef;
    --paper: #ececec;
    --card: #f0f0f0;
    --ink: #1e1e1e;
    --text: #333333;
    --green: #6cb842;
    --white: #ffffff;
  }
  * { margin: 0; padding: 0; box-sizing: border-box; }
  html, body {
    width: 1200px; height: 1000px; overflow: hidden;
    background: var(--backdrop);
  }
  .stationery { position: relative; width: 1200px; height: 1000px; }

  .wordmark {
    font-family: "Barlow", "Helvetica Neue", Arial, sans-serif;
    font-weight: 600;
    letter-spacing: 0.01em;
    white-space: nowrap;
    line-height: 1;
  }
  .tagline {
    font-family: "Zilla Slab", Georgia, serif;
    font-style: italic;
    white-space: nowrap;
    line-height: 1;
  }

  /* Letterhead */
  .letterhead {
    position: absolute; left: 135px; top: 190px;
    width: 458px; height: 620px;
    background: var(--paper);
  }
  .letterhead .brand {
    position: absolute; right: 173px; top: 20px;
    text-align: right;
  }
  .letterhead .wordmark { font-size: 10px; color: var(--ink); }
  .letterhead .tagline { font-size: 4.6px; color: var(--text); margin-top: 2px; }

  /* Business card front */
  .card {
    position: absolute; left: 644px;
    width: 422px; height: 241px;
  }
  .card-front { top: 297px; background: var(--card); }
  .card-front .brand {
    position: absolute; right: 38px; top: 28px; text-align: right;
  }
  .card-front .wordmark { font-size: 30px; color: var(--ink); }
  .card-front .tagline { font-size: 13px; color: var(--text); margin-top: 4px; }

  .contact {
    position: absolute; top: 194px;
    font-family: "Zilla Slab", Georgia, serif;
    font-size: 11.5px; line-height: 15px;
    color: var(--text); white-space: nowrap;
  }
  .contact-credentials { right: 277px; text-align: right; }
  .contact-reach { left: 173px; text-align: left; }

  /* Business card back */
  .card-back {
    top: 569px; height: 240px;
    background: var(--green);
  }
  .card-back .wordmark {
    position: absolute; left: 37px; top: 108px;
    font-size: 30px; color: var(--white);
  }
</style>
</head>
<body>
<main class="stationery">
  <section class="letterhead" aria-label="Letterhead">
    <div class="brand">
      <div class="wordmark">VORTIG PLUMBING &amp; GAS</div>
      <div class="tagline">Commercial, Domestic &amp; Maintenance</div>
    </div>
  </section>

  <section class="card card-front" aria-label="Business card front">
    <div class="brand">
      <div class="wordmark">VORTIG PLUMBING &amp; GAS</div>
      <div class="tagline">Commercial, Domestic &amp; Maintenance</div>
    </div>
    <div class="contact contact-credentials">
      <div>Licence No. 617394K</div>
      <div>ABN 47215830962</div>
    </div>
    <div class="contact contact-reach">
      <div>041-738-2956</div>
      <div>vortigplumbingandgas@corvanet.com</div>
    </div>
  </section>

  <section class="card card-back" aria-label="Business card back">
    <div class="wordmark">VORTIG PLUMBING &amp; GAS</div>
  </section>
</main>
</body>
</html>
```